Website redesign for KestrelFinPro/TrailCoinPal

Job Title: Talented Web Designer for SEO-Friendly Website Creation & HostMarlow cPanel Integration
 
Inspiration: dunerevtrack.example
Pages:

About
Get a Quote
FAQ
Boat Loans
RV Loans
Testimonials
News/Blog
Affiliate Program
Contact

Job Description:
 
We are seeking a skilled and creative freelance web designer to build a stunning, SEO-optimized website for our business. The ideal candidate will have a strong design portfolio, technical expertise in creating search engine-friendly websites, and experience implementing websites into HostMarlow cPanel.
 
Project Overview:
 
Objective: Create a modern, motorsports themed visually appealing website that is optimized for SEO.

Platform: The site will be hosted on HostMarlow, so familiarity with their cPanel for setup and integration is essential.

Deliverables:
         •A fully functional website (desktop and mobile) with user-friendly navigation and a responsive design.
         •SEO best practices implemented throughout, including proper meta tags, optimized images, fast loading speeds, and mobile compatibility.
         •Seamless integration into HostMarlow cPanel for hosting.
         •Guidance or documentation on maintaining the site post-launch.
 
Key Skills Required:
 
         •Proficiency in web design (HTML, CSS, JavaScript, or relevant platforms like WordPress).
         •Knowledge of SEO principles and tools for website optimization.
         •Experience with HostMarlow cPanel, including file management and DNS settings.
         •Strong communication skills to understand our vision and provide progress updates.
 
What We’re Looking For:
 
         •A designer who can transform our ideas into a sleek and functional website.
         •Someone proactive in suggesting creative design elements and SEO improvements.
         •A reliable professional who can meet deadlines and deliver a polished product.
 
Please provide:
 
         1.A brief introduction and why you’re a good fit for this project.
         2.Examples of previous web design projects, especially those with SEO implementation.
         3.Your estimated timeline and cost for this project.
 
We are excited to work with a talented designer who can bring our vision to life. If you are passionate about web design and SEO, we’d love to hear from you!

Target Market(s)

Boat and RV buyers looking for a loan

Coding

Number of Pages Required

5+ page

Colors
F0912C
F2A743
F7CA91
FBE8D2
FDF5EE

Requirements
Must have
• motorsports type design
Nice to have
• fcontact forms easy to use layout on brand and color scheme of kestrelfinpro and trailcoinpal.example

```html
<!DOCTYPE html>
<html lang="en">
<head>
<meta charset="utf-8">
<title>KestrelFinPro – Boat Loans Made Easy</title>
<link rel="stylesheet" href="https://fonts.googleapis.com/css2?family=Anton&family=Poppins:ital,wght@0,400;0,500;0,600;0,700;1,500;1,600&display=swap">
<style>
:root{
  --orange:#F0912C;
  --orange-deep:#E07A14;
  --orange-mid:#F2A743;
  --peach:#F7CA91;
  --cream:#FBE8D2;
  --ivory:#FDF5EE;
  --ink:#1B1B1B;
  --ink-soft:#2A2A2A;
  --grey-bg:#F1F1F1;
  --text:#333;
  --muted:#777;
  --white:#fff;
}
*{box-sizing:border-box;margin:0;padding:0}
html,body{width:1200px;height:2797px;overflow:hidden}
body{font-family:"Poppins",sans-serif;color:var(--text);background:var(--white);position:relative}
.heading{font-family:"Anton",sans-serif;text-transform:uppercase;font-weight:400;letter-spacing:.5px;line-height:1.15}
.eyebrow{color:var(--orange);font-size:13px;font-weight:500}
section,header,footer{position:absolute;left:0;width:1200px}

/* Button */
.btn{display:inline-flex;align-items:center;gap:6px;position:relative;font-size:12px;font-weight:600;color:var(--ink);padding:8px 12px 8px 14px;z-index:0;white-space:nowrap}
.btn::before{content:"";position:absolute;left:0;top:0;width:30px;height:100%;background:var(--orange);transform:skewX(-12deg);z-index:-1}
.btn svg{width:9px;height:9px}

/* Header */
.site-header{top:0;height:74px;display:flex;align-items:center;padding:0 150px 0 160px;background:var(--white);border-bottom:1px solid #eee}
.brand{display:flex;align-items:center;gap:8px;font-weight:700;font-size:19px;color:var(--orange);white-space:nowrap}
.brand-dot{width:14px;height:14px;background:var(--orange);border-radius:50%}
.main-nav{display:flex;gap:22px;font-size:12px;color:#444;margin-left:auto;align-items:center;white-space:nowrap}
.main-nav .btn{margin-left:4px;font-weight:500}

/* Hero */
.hero{top:74px;height:436px;overflow:hidden}
.hero-photo{position:absolute;inset:0;background:linear-gradient(115deg,#0e2b25 0%,#1f5a45 35%,#2f8a5e 60%,#1d6b56 80%,#123f3a 100%);clip-path:polygon(0 0,100% 0,100% 88%,85% 92%,70% 89%,55% 95%,40% 90%,25% 96%,10% 91%,0 95%)}
.hero-copy{position:absolute;left:232px;top:100px;padding-left:30px;border-left:3px solid var(--orange);width:420px}
.hero-copy h1{font-size:60px;color:var(--orange);line-height:1.1}
.hero-copy p{color:var(--white);font-size:14px;line-height:1.55;margin:12px 0 16px;width:290px}
.hero-copy .btn{color:var(--white)}

/* Calculator */
.calculator{top:510px;height:80px;display:flex;justify-content:center;align-items:center;gap:16px}
.field{width:190px;height:34px;border:1px solid #e2e2e2;border-left:3px solid var(--orange);font-size:11px;color:#aaa;display:flex;align-items:center;padding-left:12px}

/* About */
.about{top:590px;height:290px}
.about-photo{position:absolute;left:190px;top:20px;width:400px;height:250px;background:radial-gradient(ellipse at 50% 50%,#d8dde2 0%,#c64b3d 45%,#8e2b25 62%,#fff 63%)}
.about-copy{position:absolute;left:640px;top:28px;width:400px}
.about-copy h2{font-size:32px;color:var(--ink);margin:4px 0 16px}
.checklist{display:grid;grid-template-columns:1fr 1fr;gap:8px 20px;list-style:none;font-size:11px;color:#333;margin-bottom:16px}
.checklist li{display:flex;gap:6px;align-items:center}
.checklist li::before{content:"→";color:var(--orange);font-size:11px}
.about-copy p{font-size:11px;line-height:1.6;color:#555}

/* Boat types */
.boat-types{top:880px;height:410px;background:var(--ink);clip-path:polygon(0 0,100% 0,100% 94%,88% 97%,72% 93%,58% 99%,44% 93%,30% 98%,16% 93%,0 97%);text-align:center;color:var(--white)}
.boat-types .eyebrow{display:block;margin-top:42px}
.boat-types h2{font-size:32px;margin:4px 0 28px}
.type-grid{display:grid;grid-template-columns:repeat(3,260px);gap:22px 30px;justify-content:center}
.type-card{display:flex;align-items:center;gap:18px;border-bottom:1px solid #333;border-right:1px solid #333;height:74px}
.type-icon{width:78px;height:74px;background:#e9e9e9;clip-path:polygon(16% 0,100% 0,84% 100%,0 100%);display:flex;align-items:center;justify-content:center}
.type-icon svg{width:40px;height:24px}
.type-card span{font-style:italic;font-weight:500;font-size:14px;text-align:left;line-height:1.3}
.boat-types .btn{margin-top:26px;color:var(--white)}

/* Finance */
.finance{top:1290px;height:290px;text-align:center}
.finance .eyebrow{display:block;margin-top:28px}
.finance h2{font-size:32px;color:var(--ink);margin:4px 0 4px}
.finance .sub{font-size:11px;color:#555}
.loan-cards{display:flex;justify-content:center;gap:30px;margin-top:24px}
.loan-card{display:flex;align-items:center;width:420px;height:150px;border-bottom:1px solid #ddd;border-right:1px solid #ddd}
.loan-photo{width:220px;height:150px;clip-path:polygon(10% 0,100% 0,90% 100%,0 100%)}
.loan-photo.boat{background:linear-gradient(160deg,#9fc0d8,#3c6d94 55%,#1e3f5e)}
.loan-photo.rv{background:linear-gradient(160deg,#e8e8e8,#b8bcc2 55%,#5f6670)}
.loan-card span{font-style:italic;font-weight:700;font-size:19px;color:var(--ink);margin-left:28px;text-align:left;line-height:1.2}

/* Reviews */
.reviews{top:1580px;height:390px;background:var(--ink);color:var(--white);text-align:center;clip-path:polygon(0 0,100% 0,100% 94%,86% 97%,70% 93%,56% 99%,42% 93%,28% 98%,14% 93%,0 97%)}
.reviews .eyebrow{display:block;margin-top:36px}
.reviews h2{font-size:30px;margin:4px 0 18px}
.review-body{position:relative;height:190px}
.review-photo{position:absolute;left:230px;top:5px;width:280px;height:170px;background:radial-gradient(ellipse,#9aa3ad 0%,#4b535c 50%,var(--ink) 72%)}
.review-text{position:absolute;left:560px;top:0;width:480px;text-align:left}
.stars{color:var(--orange);font-size:14px;letter-spacing:3px}
.review-text p{font-size:10.5px;line-height:1.6;color:#ccc;margin:8px 0 12px}
.reviewer{display:flex;align-items:center;gap:10px}
.avatar{width:30px;height:30px;border-radius:50%;background:#6b6b6b;border:2px solid var(--white)}
.reviewer b{display:block;color:var(--orange);font-size:11px;font-weight:600}
.reviewer small{font-size:10px;color:#ccc}
.reviews .btn{color:var(--white)}

/* Blogs */
.blogs{top:1970px;height:360px;text-align:center}
.blogs .eyebrow{display:block;margin-top:26px}
.blogs h2{font-size:30px;color:var(--ink);margin:4px 0 18px}
.blog-grid{display:flex;justify-content:center;gap:24px}
.blog-card{position:relative;width:280px;height:190px;text-align:left;color:var(--white)}
.blog-card.one{background:linear-gradient(180deg,#3a6fb0,#b8c4cf 45%,#3b3f46)}
.blog-card.two{background:linear-gradient(180deg,#9ec3e3,#4d6e8e 45%,#c9a81c 70%,#1f3650)}
.blog-card.three{background:linear-gradient(180deg,#5b6d86,#c9ccd1 45%,#2a2f36)}
.date{position:absolute;left:10px;top:10px;background:var(--orange);padding:4px 8px;font-size:9px;line-height:1.2}
.date b{display:block;font-size:14px}
.blog-card h3{position:absolute;left:18px;bottom:14px;right:18px;font-size:12px;font-weight:600;line-height:1.35}
.blogs .btn{margin-top:20px}

/* Brands */
.brands{top:2330px;height:240px;background:var(--grey-bg);text-align:center}
.badge{position:absolute;right:30px;top:-30px;width:80px;height:80px;border-radius:50%;background:var(--white);border:6px solid #c2362b;box-shadow:0 0 0 3px #e0b24a}
.brands .eyebrow{display:block;margin-top:32px}
.brands h2{font-size:30px;color:var(--ink);margin:4px 0 22px}
.brand-row{display:flex;justify-content:center;gap:20px}
.brand-tile{width:150px;height:96px;background:var(--white);clip-path:polygon(8% 0,100% 0,92% 100%,0 100%);display:flex;align-items:center;justify-content:center}
.brand-tile i{display:block;width:70px;height:30px;border-radius:4px;background:#cfd3da}
.brand-tile:nth-child(3) i{width:40px;height:40px;border-radius:50%;background:var(--orange-mid)}
.brand-tile:nth-child(4) i{background:#6f84b3}

/* Footer */
.site-footer{top:2557px;height:240px;background:#0c0c0c;color:#ccc;clip-path:polygon(0 6%,14% 0,30% 5%,46% 1%,62% 6%,78% 0,100% 5%,100% 100%,0 100%)}
.footer-brand{position:absolute;top:30px;left:0;width:100%;display:flex;justify-content:center}
.footer-cols{position:absolute;top:74px;left:230px;display:flex;gap:60px;font-size:10px}
.footer-cols h4{color:var(--orange);font-size:11px;font-weight:600;margin-bottom:10px}
.contact-list{list-style:none;display:flex;flex-direction:column;gap:8px;width:180px}
.contact-list li{display:flex;gap:6px;align-items:flex-start;line-height:1.5}
.contact-list svg{width:10px;height:10px;flex:none;margin-top:2px}
.links{display:grid;grid-template-columns:60px 60px;gap:4px 20px;list-style:none;width:140px}
.links li:first-child{color:var(--orange);text-decoration:underline}
.signup{width:230px}
.signup h4{margin-bottom:2px}
.signup small{font-size:9px;color:#aaa}
.email{border-bottom:1px solid #444;padding:10px 0 6px;margin:6px 0 12px;color:#888}
.signup .btn{color:var(--white);font-size:11px}
.social{display:flex;flex-direction:column;gap:10px;margin-left:30px}
.social span{width:18px;height:18px;border:1px solid #555}
.copyright{position:absolute;bottom:0;left:0;width:100%;height:24px;background:var(--orange);color:var(--white);font-size:9px;display:flex;align-items:center;justify-content:center}
</style>
</head>
<body>

<header class="site-header">
  <div class="brand"><span class="brand-dot"></span>KestrelFinPro</div>
  <nav class="main-nav">
    <span>About</span><span>FAQ</span><span>Boat Loans</span><span>RV Loans</span><span>Blogs</span><span>Affiliate Program</span><span>Contact</span>
    <span class="btn">Get a Quote <svg viewBox="0 0 10 10"><path d="M2 8L8 2M3 2h5v5" stroke="currentColor" stroke-width="1.5" fill="none"/></svg></span>
  </nav>
</header>

<section class="hero">
  <div class="hero-photo" role="img" aria-label="Photo of a deck boat cruising on green water"></div>
  <div class="hero-copy">
    <h1 class="heading">Boat Loans<br>Made Easy!</h1>
    <p>Welcome to KestrelFinPro.com, your one-stop resource for all of your boat financing needs.</p>
    <span class="btn">Apply Today <svg viewBox="0 0 10 10"><path d="M2 8L8 2M3 2h5v5" stroke="currentColor" stroke-width="1.5" fill="none"/></svg></span>
  </div>
</section>

<section class="calculator">
  <div class="field">Loan Amount</div>
  <div class="field">Rate (APR)</div>
  <div class="field">Term (Years)</div>
  <span class="btn">Calculate Payment <svg viewBox="0 0 10 10"><path d="M2 8L8 2M3 2h5v5" stroke="currentColor" stroke-width="1.5" fill="none"/></svg></span>
</section>

<section class="about">
  <div class="about-photo" role="img" aria-label="Photo of a red and white speedboat with a rider"></div>
  <div class="about-copy">
    <span class="eyebrow">About Us</span>
    <h2 class="heading">Your Trusted Source For<br>Marine Financing.</h2>
    <ul class="checklist">
      <li>Loans From $25,000 - $5M</li><li>Quick Funding</li>
      <li>Up To 25yrs Old</li><li>Private Party Or Dealer</li>
      <li>Same-Day Approvals</li><li>Best Rates In The Industry</li>
    </ul>
    <p>Our Goal Is To Make Your Boat Purchase As Quick And Stress-Free As Possible. Our Numerous Lender Relationships Allow Us To Offer Competitive Rates And Terms With Quick Turn-Around Times.</p>
  </div>
</section>

<section class="boat-types">
  <span class="eyebrow">Apply Now</span>
  <h2 class="heading">We Finance All Types Of Boats!</h2>
  <div class="type-grid">
    <div class="type-card"><div class="type-icon"><svg viewBox="0 0 40 24"><path d="M2 16h34l-4 6H7zM10 16l4-8h12l4 8M14 8l2-5" stroke="#333" stroke-width="1.5" fill="none"/></svg></div><span>Performance<br>Boats</span></div>
    <div class="type-card"><div class="type-icon"><svg viewBox="0 0 40 24"><path d="M2 16h34l-4 6H7zM12 16V8h14l4 8" stroke="#333" stroke-width="1.5" fill="none"/></svg></div><span>Center<br>Consoles</span></div>
    <div class="type-card"><div class="type-icon"><svg viewBox="0 0 40 24"><path d="M2 16h34l-4 6H7zM14 16l2-6h10l3 6M20 10V3h8" stroke="#333" stroke-width="1.5" fill="none"/></svg></div><span>Tow<br>Boats</span></div>
    <div class="type-card"><div class="type-icon"><svg viewBox="0 0 40 24"><path d="M4 14h32M4 20h32M8 14v6M32 14v6M8 14V6h24v8" stroke="#333" stroke-width="1.5" fill="none"/></svg></div><span>Pontoons</span></div>
    <div class="type-card"><div class="type-icon"><svg viewBox="0 0 40 24"><path d="M2 16h34l-4 6H7zM12 16V9h12v7M24 9l8-7" stroke="#333" stroke-width="1.5" fill="none"/></svg></div><span>Fishing<br>Boats</span></div>
    <div class="type-card"><div class="type-icon"><svg viewBox="0 0 40 24"><path d="M2 17h36l-5 5H6zM8 17l3-6h18l4 6M13 11l3-5h10l2 5" stroke="#333" stroke-width="1.5" fill="none"/></svg></div><span>Yachts &amp;<br>much more!</span></div>
  </div>
  <span class="btn">Apply Today <svg viewBox="0 0 10 10"><path d="M2 8L8 2M3 2h5v5" stroke="currentColor" stroke-width="1.5" fill="none"/></svg></span>
</section>

<section class="finance">
  <span class="eyebrow">Finance</span>
  <h2 class="heading">We Finance More Than Just Boats</h2>
  <p class="sub">At Harborline Leisure Finance, We Are Your One-Stop Resource For All Marine, RV And Airplane Financing</p>
  <div class="loan-cards">
    <div class="loan-card"><div class="loan-photo boat" role="img" aria-label="Photo of a white bowrider boat on the water"></div><span>Boat<br>Loans</span></div>
    <div class="loan-card"><div class="loan-photo rv" role="img" aria-label="Photo of a class C motorhome"></div><span>RV<br>Loans</span></div>
  </div>
</section>

<section class="reviews">
  <span class="eyebrow">Reviews</span>
  <h2 class="heading">What Our Customers Say</h2>
  <div class="review-body">
    <div class="review-photo" role="img" aria-label="Photo of boat engines on a transom"></div>
    <div class="review-text">
      <div class="stars">★★★★★</div>
      <p>Just Purchased A Boat And Used Harborline And They Made The Process Very Easy. Tessa Varlow Helped Every Step Of The Way And Was Always Available When I Had Any Questions. She Was Quick To Keep Me Updated And Streamlined The Entire Process Of Paperwork And Funding. I Would Highly Recommend Using Harborline Based On My Purchasing Experience. Ask For Tessa And She Will Not Let You Down. Will Definitely Use Again When Buying My Next Boat. They Made The Process Very Easy And Streamlined The Entire Process.</p>
      <div class="reviewer"><span class="avatar"></span><div><b>Dale Merrin</b><small>Albany</small></div></div>
    </div>
  </div>
  <span class="btn">View All <svg viewBox="0 0 10 10"><path d="M2 8L8 2M3 2h5v5" stroke="currentColor" stroke-width="1.5" fill="none"/></svg></span>
</section>

<section class="blogs">
  <span class="eyebrow">Latest articles</span>
  <h2 class="heading">Our Blogs</h2>
  <div class="blog-grid">
    <article class="blog-card one" role="img" aria-label="Photo of a travel trailer and pickup truck"><div class="date">Dec 10<b>2024</b></div><h3>Lorem Ipsum Is Simply Dummy Text Of The Printing And Typesetting Industry...</h3></article>
    <article class="blog-card two" role="img" aria-label="Photo of a yellow speedboat on a lake"><div class="date">Dec 10<b>2024</b></div><h3>Lorem Ipsum Is Simply Dummy Text Of The Printing And Typesetting Industry...</h3></article>
    <article class="blog-card three" role="img" aria-label="Photo of outboard engines close up"><div class="date">Dec 10<b>2024</b></div><h3>Lorem Ipsum Is Simply Dummy Text Of The Printing And Typesetting Industry...</h3></article>
  </div>
  <span class="btn">View All <svg viewBox="0 0 10 10"><path d="M2 8L8 2M3 2h5v5" stroke="currentColor" stroke-width="1.5" fill="none"/></svg></span>
</section>

<section class="brands">
  <div class="badge" aria-hidden="true"></div>
  <span class="eyebrow">Lorem ipsum</span>
  <h2 class="heading">Our Brands</h2>
  <div class="brand-row">
    <div class="brand-tile"><i></i></div>
    <div class="brand-tile"><i></i></div>
    <div class="brand-tile"><i></i></div>
    <div class="brand-tile"><i></i></div>
    <div class="brand-tile"><i></i></div>
  </div>
</section>

<footer class="site-footer">
  <div class="footer-brand"><div class="brand"><span class="brand-dot"></span>KestrelFinPro</div></div>
  <div class="footer-cols">
    <div>
      <h4>CONTACT US</h4>
      <ul class="contact-list">
        <li><svg viewBox="0 0 10 10"><path d="M2 1l2 2-1 1.5a6 6 0 0 0 2.5 2.5L7 6l2 2-1.5 1.5C4 9 1 6 .5 2.5z" fill="#F0912C"/></svg>(555) 014-2270</li>
        <li><svg viewBox="0 0 10 10"><rect x="1" y="2" width="8" height="6" fill="none" stroke="#F0912C"/><path d="M1 2l4 3 4-3" fill="none" stroke="#F0912C"/></svg>marina@kestrelfinpro.example</li>
        <li><svg viewBox="0 0 10 10"><path d="M5 0a3.5 3.5 0 0 1 3.5 3.5C8.5 6 5 10 5 10S1.5 6 1.5 3.5A3.5 3.5 0 0 1 5 0z" fill="#F0912C"/></svg>418 Tidewater Way Ste. 210, Port Alder, CA 90000</li>
      </ul>
    </div>
    <div>
      <h4>QUICK LINKS</h4>
      <ul class="links">
        <li>Home</li><li>Testimonials</li><li>About</li><li>Blogs</li><li>FAQ</li><li>Affiliate</li><li>Boat Loans</li><li>Program</li><li>RV Loans</li><li>Contact</li>
      </ul>
    </div>
    <div class="signup">
      <h4>SIGN UP AND SAVE!</h4>
      <small>Exclusive Email Offers &amp; Limited Time</small>
      <div class="email">Enter Email</div>
      <span class="btn">Subscribe <svg viewBox="0 0 10 10"><path d="M2 8L8 2M3 2h5v5" stroke="currentColor" stroke-width="1.5" fill="none"/></svg></span>
    </div>
    <div class="social"><span></span><span></span><span></span></div>
  </div>
  <div class="copyright">© 2024 KestrelFinPro. All rights reserved</div>
</footer>

</body>
</html>
```